Business Card

I need a business card for my work as an energy lawyer. I am a single prctioner and I consult to energy companies regarding a variety of legal issues involving environmental matters, energy efficiency, regulations and contractual arrangements. i need a distinctive business card that stands out and is easy to read. I like bold colors or high contrast. I like a sparse architectural design. The font should be easy to read (many of my clients use reading glasses and are concerned about small type). The card should communicate that I am somewhat different from ordinary legal counsel. Below are some examples of cards that I like. Thank you for your interest and thought. Glenn Dusty Harker
Updates

Thanks to everyone who has submitted a design.  My general comments are:

1.  I like the colourful cards and the high contrast cards.
2.  I prefer the use of icons for home address, phone, mobile and email.
3.  For the high contrast cards please use three colours - black background, and red and white for the logo or information.
4.  The mobile number area code should be 403 and not 404.
5.  I also need to add a direct phone line which is 403-517-6392.

Thank you,

Glenn Harker

Reason: I have briefly extended the deadline by three days to allow those individuals who responded early to revise their designs based upon the subsequent clarification of the colours (red, white, black background) and the request to use icons and add a direct phone number.

Industry/Entity Type

Business

```html
<!DOCTYPE html>
<html lang="en">
<head>
<meta charset="utf-8">
<title>Glenn Dusty Harker — Business Card</title>
<link href="https://fonts.googleapis.com/css2?family=Open+Sans:wght@400&display=swap" rel="stylesheet">
<style>
  :root {
    --backdrop: #e9e7e4;
    --card: #ffffff;
    --label: #111111;
    --value: #676767;
    --accent: #00ff00;
  }
  * { margin: 0; padding: 0; box-sizing: border-box; }
  html, body {
    width: 1200px;
    height: 900px;
    overflow: hidden;
    background: var(--backdrop);
  }
  .card {
    position: absolute;
    left: 69px;
    top: 155px;
    width: 1063px;
    height: 590px;
    background: var(--card);
  }
  .contact-list {
    position: absolute;
    left: 106px;
    top: 140px;
    list-style: none;
    font-family: "Open Sans", Arial, sans-serif;
    font-weight: 400;
    font-size: 48px;
    line-height: 60px;
    letter-spacing: 6px;
    white-space: nowrap;
  }
  .contact-label { color: var(--label); }
  .contact-value { color: var(--value); }
  .at-sign { color: var(--accent); }
  .accent-bar {
    position: absolute;
    right: 0;
    bottom: 0;
    width: 362px;
    height: 16px;
    background: var(--accent);
  }
</style>
</head>
<body>
  <main class="card" aria-label="Business card of Glenn Dusty Harker">
    <ul class="contact-list">
      <li><span class="contact-label">Address:</span> <span class="contact-value">2274 Larch Street N.W.,</span></li>
      <li><span class="contact-value">Calgary, Alberta</span></li>
      <li><span class="contact-label">Phone:</span> <span class="contact-value">1.403.517.6392</span></li>
      <li><span class="contact-label">Mobile:</span> <span class="contact-value">1.403.829.4516</span></li>
      <li><span class="contact-label">email:</span> <span class="contact-value">dusty<span class="at-sign">@</span>dustyharker.com</span></li>
    </ul>
    <div class="accent-bar"></div>
  </main>
</body>
</html>
```